SLA & Internet Advert

Advertise some of our key SLA services & Internet Connectivity services.
Service Level Agreement:
Unlimited Remote, Email, Helpdesk & Telephone Support.
Unlimited Service Calls
Support Hours Monday - Saturday 7am-10pm Sunday till 5pm
Free additional visits during ofsted periods
Free remote access to school server for staff members
Free mobile device management for tablet devices
Free Email&Webhosting Service
Remote support on every device in school allowing us to close 90% of tickets within 30 mins.
Service Level Agreement Package 1 - Includes all the above + 1 Site visit every 2 weeks £2,500 per annum
Service Level Agreement Package 2 - Includes all the above + 1 Site Visit every week £4,500 per annum
Service Level Agreement Package 3 - Includes all the above + 2 Site visits every week - £7,540 per annum
Internet Connectivity (medium/large Primary)
Managed Firewall
Managed Web filter & Safeguarding
User reporting portal/email reporting.
Main Internet Line 1000 mb/s download 100mb/s upload
Back up Internet Line 80mb/s download 20mb/s upload
100% uptime guaranteed.
£3000 per annum
Internet Connectivity (Small Primary School)
Managed Firewall
£2100 per annum
My website is https://www.kolvarnet.co.uk if you need any further information like phone numbers / email address etc
Target Market(s)
Education
Look and feel
Each slider illustrates characteristics of the customer's brand and the style your logo design should communicate.

```html
<!DOCTYPE html>
<html lang="en">
<head>
<meta charset="utf-8">
<title>SLA &amp; Internet Connectivity Flyer</title>
<link rel="stylesheet" href="https://fonts.googleapis.com/css2?family=Rubik:wght@300;400;500;600;700&family=Encode+Sans+Semi+Condensed:wght@400;500;600&display=swap">
<style>
  :root{
    --navy:#0f2c52;
    --navy-deep:#0b2345;
    --orange:#f2530f;
    --orange-soft:#f47a2d;
    --blue:#1e78d6;
    --grey-panel:#d9dadc;
    --grey-line:#c8cbd0;
    --white:#ffffff;
    --bronze-a:#8a5533;--bronze-b:#d9a577;
    --silver-a:#b9bcc0;--silver-b:#f4f4f4;
    --gold-a:#a98f3c;--gold-b:#e8d389;
    --page-bg:#ececec;
  }
  *{box-sizing:border-box;margin:0;padding:0}
  html,body{width:1200px;height:2483px;overflow:hidden;background:var(--page-bg)}
  body{position:relative;font-family:"Rubik",sans-serif;color:var(--navy)}
  .flyer{position:absolute;left:0;top:392px;width:940px;height:1330px;background:var(--white);
    transform:scale(1.2766);transform-origin:0 0;overflow:hidden}
  .abs{position:absolute}

  .brand{left:55px;top:62px}
  .brand-name{font-weight:700;font-size:42px;color:var(--blue);letter-spacing:1px;line-height:1;display:flex;align-items:center;gap:10px}
  .brand-name .dot{width:22px;height:22px;background:var(--orange);display:inline-block}
  .brand-tag{font-size:12px;color:var(--blue);letter-spacing:.8px;margin-top:8px}

  .hero-art{left:0;top:0;width:940px;height:480px}
  .headline{left:57px;top:172px;font-weight:600;font-size:39px;line-height:38px;text-transform:uppercase}
  .headline .l1{color:var(--orange)}
  .headline .l2,.headline .l3{color:var(--blue)}
  .headline .l4{color:var(--white)}

  .sla-frame{left:25px;top:396px;width:872px;height:310px;border:1.5px solid var(--grey-line);border-radius:18px}
  .sla-title{left:42px;top:378px;width:460px;height:46px;background:var(--orange);border-radius:23px;color:var(--white);
    font-weight:500;font-size:27px;line-height:46px;padding-left:27px;letter-spacing:.3px}
  .sla-list{left:58px;top:444px;width:350px;list-style:none;font-weight:600;font-size:15.5px;line-height:19px;letter-spacing:.3px}
  .sla-list li{position:relative;padding-left:23px;margin-bottom:8px}
  .sla-list li svg{position:absolute;left:0;top:3px}

  .inset-photo{left:480px;top:332px;width:190px;height:180px}

  .hours{left:451px;top:530px;display:flex;gap:18px;align-items:flex-start}
  .hours-label{color:var(--orange);font-weight:700;font-size:22px;line-height:22px}
  .hours-times{font-weight:400;font-size:26px;line-height:24px;color:var(--navy)}

  .remote{left:440px;top:597px;width:434px;height:84px;border-radius:14px;background:var(--navy);overflow:hidden;box-shadow:0 6px 8px rgba(0,0,0,.15)}
  .remote-text{position:absolute;left:14px;top:14px;color:var(--white);font-weight:600;font-size:17px;line-height:18.5px;letter-spacing:.4px}
  .remote-stat{position:absolute;right:0;top:0;width:125px;height:84px;background:var(--orange);color:var(--white);text-align:center}
  .remote-stat b{display:block;font-weight:700;font-size:40px;line-height:40px;margin-top:8px}
  .remote-stat span{display:block;font-size:10px;font-weight:600;line-height:11px}

  .pkg{top:722px;width:270px;height:206px;border-radius:12px;background:var(--navy);overflow:hidden;color:var(--white);text-align:center}
  .pkg-head{height:56px;color:var(--navy);font-weight:600;font-size:16px;line-height:16px;padding-top:12px;text-transform:uppercase}
  .pkg-1 .pkg-head{background:linear-gradient(180deg,var(--bronze-a),var(--bronze-b));color:#3a2414}
  .pkg-2 .pkg-head{background:linear-gradient(180deg,var(--silver-b),var(--silver-a))}
  .pkg-3 .pkg-head{background:linear-gradient(180deg,var(--gold-a),var(--gold-b));color:#2d2a14}
  .pkg-inc{font-weight:600;font-size:16.5px;margin-top:15px;letter-spacing:.2px}
  .pkg-plus{margin:3px auto 0;display:block}
  .pkg-visit{font-weight:700;font-size:21px;line-height:21px;margin-top:2px}
  .pkg-price{display:inline-block;margin-top:8px;border-radius:15px;padding:0 14px;height:30px;line-height:30px;font-weight:600;font-size:15px;color:var(--navy);min-width:178px}
  .pkg-1 .pkg-price{background:linear-gradient(90deg,#c97d4e,#e8a06e)}
  .pkg-2 .pkg-price{background:var(--white)}
  .pkg-3 .pkg-price{background:linear-gradient(90deg,#cbb566,#efdf9a)}

  .net{top:948px;width:411px;height:258px;border-radius:12px;background:var(--grey-panel)}
  .net-head{height:66px;border-radius:12px 12px 0 0;color:var(--white);text-align:center;padding-top:10px}
  .net-head h2{font-weight:600;font-size:25px;line-height:26px;text-transform:uppercase}
  .net-head p{font-weight:600;font-size:15px;text-transform:uppercase}
  .net-a .net-head{background:var(--orange)}
  .net-a .net-head p{color:#fff0e6}
  .net-b .net-head{background:var(--navy)}
  .net-list{list-style:none;padding:8px 0 0 16px;font-family:"Encode Sans Semi Condensed",sans-serif;font-size:15.5px;color:#1f2530;line-height:19px}
  .net-list li{position:relative;padding-left:18px;margin-bottom:8px}
  .net-list li::before{content:"";position:absolute;left:0;top:5px;width:9px;height:9px;border-radius:50%;background:var(--navy)}
  .net-list em{font-style:normal;color:var(--orange)}
  .net-price{left:50%;bottom:-20px;transform:translateX(-50%);width:244px;height:42px;border-radius:8px;color:var(--white);font-weight:600;font-size:22px;line-height:42px;text-align:center;letter-spacing:.3px}
  .net-a .net-price{background:var(--navy)}
  .net-b .net-price{background:var(--orange)}

  .footer{left:0;top:1253px;width:940px;height:77px}
  .footer-text{top:1253px;height:77px;line-height:77px;color:var(--white);font-weight:500;font-size:19px;display:flex;align-items:center;gap:8px;letter-spacing:.4px}
</style>
</head>
<body>
<div class="flyer">

  <svg class="abs hero-art" viewBox="0 0 940 480" aria-hidden="false">
    <path d="M0 150 H450 C420 200 430 290 470 345 C420 348 380 350 0 350 Z" fill="var(--navy)"/>
    <path d="M418 0 C360 120 380 280 470 345" fill="none" stroke="var(--orange)" stroke-width="6"/>
    <path d="M432 0 C378 120 396 272 480 336" fill="none" stroke="var(--blue)" stroke-width="4"/>
    <g role="img" aria-label="Photo of school pupils in uniform working at laptops in a classroom">
      <path d="M440 0 H940 V400 C860 460 720 480 600 440 C470 400 380 250 440 0 Z" fill="url(#photoTone)"/>
    </g>
    <defs>
      <linearGradient id="photoTone" x1="0" y1="0" x2="1" y2="1">
        <stop offset="0" stop-color="#8f9a86"/>
        <stop offset=".5" stop-color="#3d4f45"/>
        <stop offset="1" stop-color="#2a3a34"/>
      </linearGradient>
    </defs>
  </svg>

  <div class="abs brand">
    <div class="brand-name"><span class="dot"></span>KOLVARNET</div>
    <div class="brand-tag">EDUCATION SUPPORT &amp; INSTALLATION</div>
  </div>

  <h1 class="abs headline">
    <span class="l1">SLA Services</span><br>
    <span class="l2">&amp; Internet</span><br>
    <span class="l3">Connectivity</span><br>
    <span class="l4">Services</span>
  </h1>

  <div class="abs sla-frame"></div>
  <div class="abs sla-title">SERVICE LEVEL AGREEMENT*</div>

  <svg class="abs inset-photo" viewBox="0 0 190 180">
    <g transform="rotate(14 95 90)">
      <rect x="20" y="15" width="150" height="150" rx="18" fill="var(--orange)"/>
      <rect x="30" y="25" width="130" height="130" rx="12" fill="#9aa7b2" role="img" aria-label="Photo of a pupil using a laptop with a robotics kit"/>
    </g>
  </svg>

  <ul class="abs sla-list">
    <li><svg width="12" height="12" viewBox="0 0 12 12"><rect x="1" y="2" width="9" height="9" fill="none" stroke="var(--orange)" stroke-width="1.3"/><path d="M3 6l2 2 6-7" fill="none" stroke="var(--orange)" stroke-width="1.5"/></svg>Unlimited Remote, Email, Helpdesk &amp; Telephone Support</li>
    <li><svg width="12" height="12" viewBox="0 0 12 12"><rect x="1" y="2" width="9" height="9" fill="none" stroke="var(--orange)" stroke-width="1.3"/><path d="M3 6l2 2 6-7" fill="none" stroke="var(--orange)" stroke-width="1.5"/></svg>Unlimited Service Calls</li>
    <li><svg width="12" height="12" viewBox="0 0 12 12"><rect x="1" y="2" width="9" height="9" fill="none" stroke="var(--orange)" stroke-width="1.3"/><path d="M3 6l2 2 6-7" fill="none" stroke="var(--orange)" stroke-width="1.5"/></svg>Free additional visits during ofsted periods</li>
    <li><svg width="12" height="12" viewBox="0 0 12 12"><rect x="1" y="2" width="9" height="9" fill="none" stroke="var(--orange)" stroke-width="1.3"/><path d="M3 6l2 2 6-7" fill="none" stroke="var(--orange)" stroke-width="1.5"/></svg>Free remote access to school server for staff members</li>
    <li><svg width="12" height="12" viewBox="0 0 12 12"><rect x="1" y="2" width="9" height="9" fill="none" stroke="var(--orange)" stroke-width="1.3"/><path d="M3 6l2 2 6-7" fill="none" stroke="var(--orange)" stroke-width="1.5"/></svg>Free mobile device management for tablet devices</li>
    <li><svg width="12" height="12" viewBox="0 0 12 12"><rect x="1" y="2" width="9" height="9" fill="none" stroke="var(--orange)" stroke-width="1.3"/><path d="M3 6l2 2 6-7" fill="none" stroke="var(--orange)" stroke-width="1.5"/></svg>Free Email&amp;Webhosting Service</li>
  </ul>

  <div class="abs hours">
    <div class="hours-label">SUPPORT<br>HOURS</div>
    <div class="hours-times">Mon - Sat:&nbsp; 7am-10pm<br>Sunday till 5pm</div>
  </div>

  <div class="abs remote">
    <div class="remote-text">REMOTE SUPPORT ON EVERY<br>DEVICE IN SCHOOL ALLOWING<br>US TO CLOSE</div>
    <div class="remote-stat"><b>90%</b><span>OF TICKETS<br>WITHIN 30 MINS</span></div>
  </div>

  <section class="abs pkg pkg-1" style="left:45px">
    <div class="pkg-head">Service Level Agreement<br>Package 1</div>
    <div class="pkg-inc">*INCLUDES ALL THE ABOVE</div>
    <svg class="pkg-plus" width="16" height="16" viewBox="0 0 16 16"><circle cx="8" cy="8" r="7" fill="none" stroke="var(--orange-soft)" stroke-width="1.3"/><path d="M8 4v8M4 8h8" stroke="var(--orange-soft)" stroke-width="1.3"/></svg>
    <div class="pkg-visit">1 SITE VISIT<br>EVERY 2 WEEKS</div>
    <div class="pkg-price"><sup>£</sup>2,500 PER ANNUM</div>
  </section>
  <section class="abs pkg pkg-2" style="left:333px">
    <div class="pkg-head">Service Level Agreement<br>Package 2</div>
    <div class="pkg-inc">*INCLUDES ALL THE ABOVE</div>
    <svg class="pkg-plus" width="16" height="16" viewBox="0 0 16 16"><circle cx="8" cy="8" r="7" fill="none" stroke="var(--orange-soft)" stroke-width="1.3"/><path d="M8 4v8M4 8h8" stroke="var(--orange-soft)" stroke-width="1.3"/></svg>
    <div class="pkg-visit">1 SITE VISIT<br>EVERY WEEK</div>
    <div class="pkg-price"><sup>£</sup>4,500 PER ANNUM</div>
  </section>
  <section class="abs pkg pkg-3" style="left:623px">
    <div class="pkg-head">Service Level Agreement<br>Package 3</div>
    <div class="pkg-inc">*INCLUDES ALL THE ABOVE</div>
    <svg class="pkg-plus" width="16" height="16" viewBox="0 0 16 16"><circle cx="8" cy="8" r="7" fill="none" stroke="var(--orange-soft)" stroke-width="1.3"/><path d="M8 4v8M4 8h8" stroke="var(--orange-soft)" stroke-width="1.3"/></svg>
    <div class="pkg-visit">2 SITE VISITS<br>EVERY WEEK</div>
    <div class="pkg-price"><sup>£</sup>7,540&nbsp; PER ANNUM</div>
  </section>

  <section class="abs net net-a" style="left:50px">
    <div class="net-head"><h2>Internet Connectivity</h2><p>(Medium/Large Primary)</p></div>
    <ul class="net-list">
      <li>Managed Firewall</li>
      <li>Managed Web filter &amp; Safeguarding</li>
      <li>User reporting portal/email reporting</li>
      <li>Main Internet Line <em>1000 mb/s</em> download <em>100mb/s</em> upload</li>
      <li>Back up Internet Line <em>80mb/s</em> download <em>20mb/s</em> upload</li>
      <li>100% uptime guaranteed</li>
    </ul>
    <div class="abs net-price"><sup>£</sup>3000 PER ANNUM</div>
  </section>

  <section class="abs net net-b" style="left:482px">
    <div class="net-head"><h2>Internet Connectivity</h2><p>(Small Primary School)</p></div>
    <ul class="net-list">
      <li>Managed Firewall</li>
      <li>Managed Web filter &amp; Safeguarding</li>
      <li>User reporting portal/email reporting</li>
      <li>Main Internet Line <em>1000 mb/s</em> download <em>100mb/s</em><br>upload</li>
    </ul>
    <div class="abs net-price"><sup>£</sup>2100 PER ANNUM</div>
  </section>

  <svg class="abs footer" viewBox="0 0 940 77">
    <rect width="940" height="77" fill="var(--navy)"/>
    <path d="M0 0 H405 L382 77 H0 Z" fill="var(--orange)"/>
  </svg>
  <div class="abs footer-text" style="left:55px">CALL US NOW!
    <svg width="14" height="14" viewBox="0 0 24 24"><path d="M6.6 10.8a15 15 0 006.6 6.6l2.2-2.2a1 1 0 011-.25 11.4 11.4 0 003.6.57 1 1 0 011 1V20a1 1 0 01-1 1A17 17 0 013 4a1 1 0 011-1h3.5a1 1 0 011 1c0 1.25.2 2.45.57 3.57a1 1 0 01-.25 1z" fill="#fff"/></svg>
    0161 555 0147</div>
  <div class="abs footer-text" style="left:412px;font-weight:400">
    <svg width="16" height="14" viewBox="0 0 16 14"><rect x="1" y="1" width="14" height="12" fill="#fff"/><path d="M1 1l7 6 7-6" fill="none" stroke="var(--navy)" stroke-width="1.4"/></svg>
    info@kolvarnet.co.uk</div>
  <div class="abs footer-text" style="left:670px;font-weight:400">
    <svg width="18" height="18" viewBox="0 0 20 20"><circle cx="10" cy="10" r="8.5" fill="none" stroke="#fff" stroke-width="1.5"/><ellipse cx="10" cy="10" rx="3.5" ry="8.5" fill="none" stroke="#fff" stroke-width="1.3"/><path d="M1.5 10h17M3 5.5h14M3 14.5h14" stroke="#fff" stroke-width="1.2"/></svg>
    www.kolvarnet.co.uk</div>

</div>
</body>
</html>
```